Painting and decorating services

A flyer that promotes my services as a high quality painter and decorator. My services are fully flexible and we cater for range of customers from the decoration of small homes through to larger businesses. We have the flexibility to work through the night which suits businesses that cannot afford to shut throughout the day. We guarantee a top quality finish and are proud to promote a loyalty scheme for successful referrals.

We are truly a family business that is proud and confident to offer one of the most reliable and friendly services on offer.

Target Market(s)

Family homes, businesses who want offer of 24/7 services

Industry/Entity Type

Painting

Font styles to use
Serif
Sans Serif

Requirements
Must have
• Promotion of reliability, value, quality, service
• Days rates and price work considered
• Promotion of night work
• Loyalty scheme / incentives offerred for referrals
• Concept that we are an extremely hard working team who work extended hours and offer flexibility to customers
• Some picture examples of high quality paint jobs as examples of my work.
• Contact details. Phone 01745382916 or mobile 0762931846 email: tkbrushandfinishworks@mailvane.com
Nice to have
• Notion of friendliness coming across from the advert.
• Commitment to giving the customer what they want and delivering to the highest specifications requested
Should not have
• Any over exaggerated false promises that would make the reader of the flyer believe it's just another blagging tradesman with false marketing and empty promises.

```html
<!DOCTYPE html>
<html lang="en">
<head>
<meta charset="utf-8">
<title>Painting and Decorating Flyer</title>
<link rel="stylesheet" href="https://fonts.googleapis.com/css2?family=Oswald:wght@500;600;700&family=Lato:wght@300;400&family=Russo+One&display=swap">
<style>
:root{
  --navy:#13294b;
  --yellow:#fbbb00;
  --charcoal:#4a4a4a;
  --paper:#ffffff;
  --ink:#1f1f1f;
  --grey-text:#444444;
  --stage:#ffffff;
}
*{margin:0;padding:0;box-sizing:border-box}
html,body{width:1200px;height:1200px;overflow:hidden;background:var(--stage)}
.stage{position:absolute;left:0;top:0;width:1500px;height:1500px;transform:scale(.8);transform-origin:0 0}
.flyer{position:absolute;left:271px;top:94px;width:934px;height:1310px;background:var(--paper);overflow:hidden}
.flyer-shapes{position:absolute;left:0;top:0;width:934px;height:1310px}
.brand{position:absolute;right:34px;top:28px;width:300px;text-align:right;font-family:'Lato',sans-serif;font-weight:400;font-size:50px;line-height:1.05;color:var(--navy);letter-spacing:1px}
.headline{position:absolute;left:28px;top:686px;width:470px;font-family:'Oswald',sans-serif;text-transform:uppercase;line-height:1;white-space:nowrap}
.headline .h-main{display:block;font-size:54px;font-weight:600;color:var(--navy);letter-spacing:-.5px}
.headline .h-sub{display:block;font-size:33px;font-weight:600;color:var(--yellow);margin-top:8px;letter-spacing:.5px}
.headline .h-end{display:block;font-size:36px;font-weight:600;color:var(--ink);margin-top:8px;letter-spacing:.5px}
.section-title{font-family:'Oswald',sans-serif;font-weight:500;color:var(--yellow);font-size:25px;line-height:1}
.about{position:absolute;left:26px;top:850px;width:460px}
.about p{font-family:'Lato',sans-serif;font-size:14.6px;line-height:18.2px;color:var(--ink);text-align:justify;margin-top:6px;hyphens:auto}
.call-now{position:absolute;left:0;top:1100px;width:500px;text-align:center;font-family:'Oswald',sans-serif;font-weight:700;font-size:50px;line-height:50px;color:var(--yellow)}
.phone-band{position:absolute;left:0;top:1144px;width:514px;height:83px;background:var(--yellow);display:flex;align-items:center;justify-content:center;font-family:'Oswald',sans-serif;font-weight:600;font-size:35px;color:var(--charcoal);letter-spacing:.3px}
.website{position:absolute;left:0;width:514px;text-align:center;top:1258px;font-family:'Lato',sans-serif;font-size:14px;letter-spacing:7px;color:var(--grey-text)}
.services{position:absolute;left:538px;top:574px;width:376px}
.services ul{list-style:none;margin-top:8px}
.services li{position:relative;padding-left:14px;font-family:'Lato',sans-serif;font-size:14.6px;line-height:18.4px;color:#fff;text-align:justify;margin-bottom:6px}
.services li::before{content:"";position:absolute;left:1px;top:6px;width:6px;height:6px;border-radius:50%;background:var(--yellow)}
.night-work{position:absolute;left:500px;top:875px;width:434px;height:145px;background:var(--yellow);text-align:center;font-family:'Oswald',sans-serif;font-weight:700;text-transform:uppercase;line-height:58px;padding-top:16px}
.night-work .nw-top{display:block;font-size:62px;color:#fff;letter-spacing:1px}
.night-work .nw-bottom{display:block;font-size:62px;color:var(--navy);letter-spacing:1px}
.hours{position:absolute;left:564px;top:1069px;width:330px;height:194px;border:3px solid var(--yellow);border-radius:14px}
.hours h3{position:absolute;left:50%;top:-26px;transform:translateX(-50%);background:var(--charcoal);padding:0 6px;font-family:'Oswald',sans-serif;font-weight:500;font-size:35px;line-height:44px;color:#fff;white-space:nowrap}
.hours dl{position:absolute;left:0;top:34px;width:100%}
.hours .row{display:flex;align-items:baseline;height:46px}
.hours dt{width:127px;text-align:right;font-family:'Lato',sans-serif;font-weight:300;font-size:28px;color:#fff}
.hours dd{margin-left:13px;font-family:'Russo One',sans-serif;font-size:25px;color:#fff}
</style>
</head>
<body>
<div class="stage">
  <div class="flyer">
    <svg class="flyer-shapes" viewBox="0 0 934 1310" xmlns="http://www.w3.org/2000/svg">
      <defs>
        <linearGradient id="photoTone" x1="0" y1="0" x2="1" y2="1">
          <stop offset="0" stop-color="#e9eef3"/>
          <stop offset=".45" stop-color="#b9cbe0"/>
          <stop offset=".75" stop-color="#c9a97a"/>
          <stop offset="1" stop-color="#f2c24a"/>
        </linearGradient>
      </defs>
      <polygon role="img" aria-label="Photo of a smiling couple painting a wall yellow with a roller and brush" fill="url(#photoTone)" points="0,0 409,0 934,421 934,446 0,620"/>
      <polygon class="stripe-navy" fill="#13294b" points="409,0 452,0 934,408 934,421"/>
      <polygon class="stripe-yellow" fill="#fbbb00" points="452,0 474,0 934,400 934,408"/>
      <polygon class="panel-dark" fill="#4a4a4a" points="449,570 934,453 934,1310 514,1310 514,636"/>
      <polygon class="band-navy" fill="#13294b" points="0,620 934,446 934,450 0,651"/>
      <polygon class="band-yellow" fill="#fbbb00" points="0,651 934,450 934,454 0,676"/>
    </svg>

    <div class="brand">TK BRUSH<br>WORKS</div>

    <h1 class="headline">
      <span class="h-main">Reliable Decorating</span>
      <span class="h-sub">For homes and businesses</span>
      <span class="h-end">Day rates and price work</span>
    </h1>

    <section class="about">
      <h2 class="section-title">About us</h2>
      <p>We are a genuine family business of painters and decorators, proud to offer one of the most reliable and friendly services around. From a single bedroom in a family home to the offices, shops and premises of larger businesses, we take on work of every size and give each job the same care. We are a hard working team who put in extended hours and fit around your plans, not the other way round. We listen to what you want, agree the details up front and work to the specification you ask for, with careful preparation, clean lines and a tidy site at the end of every day. Day rates and price work are both considered, so you can choose what suits your budget. Recommend us to a friend and, when the job goes ahead, our loyalty scheme gives you a thank you on your next project.</p>
    </section>

    <div class="call-now">CALL NOW</div>
    <div class="phone-band">01745382916 OR 0762931846</div>
    <div class="website">www.tkbrushworks-decor.com</div>

    <section class="services">
      <h2 class="section-title">Our services</h2>
      <ul>
        <li>Interior and exterior painting for homes of all sizes, from one room to the whole house,</li>
        <li>commercial decorating for offices, shops and premises that need to stay open by day.</li>
        <li>Wallpapering, woodwork, ceilings and careful surface preparation before every coat,</li>
        <li>day rates or fixed price work agreed before we start, with a finish checked with you before we call the job done</li>
        <li>and a loyalty scheme that rewards you for every successful referral you send our way</li>
      </ul>
    </section>

    <div class="night-work">
      <span class="nw-top">Night work</span>
      <span class="nw-bottom">Available</span>
    </div>

    <section class="hours">
      <h3>opening hours</h3>
      <dl>
        <div class="row"><dt>mon:</dt><dd>00 to 00</dd></div>
        <div class="row"><dt>tues:</dt><dd>00 to 00</dd></div>
        <div class="row"><dt>wed:</dt><dd>00 to 00</dd></div>
      </dl>
    </section>
  </div>
</div>
</body>
</html>
```